Label Design for American Pet Health Startup

We need your help in creating a line-up of labels for our upcoming products. The products will come in two different sizes/shapes. We have a logo (sourced form GraphiHive!) to start from and a pretty extensive brief (see attached.) The winning design will be bold, simple, and create a strongly branded look to the whole line while allowing consumers to easily sort through the different SKUs.

The logo and other existing design elements are in the attached powerpoint. I will also post some of the source files.

If you choose to compete for this project, please read the creative brief and the powerpoint very carefully before starting.

Thank you for your time and consideration.

Target Market(s)

Pet owners (dog owners, initially) who care deeply about their pets. Their pets are older and may not be thriving the way they once were. The owners want their pets to have the highest quality of life possible, for as long as is practical. They take their pets frequently to the vet and have great faith in veterinary medicine, but they also believe that dietary supplements may have a beneficial effect. They believe this to be possible because they take supplements themselves.

They are probably older--empty nesters or soon to be. They’ve owned their dog for five years or more, or have rescued an older dog from a shelter. Their dog is, in many ways, a full member of their family.

Industry/Entity Type

Pet Care

Font styles to use
Sans Serif

Requirements
Must have
• Please see the attached brief for this detail. I have cut and paste it into this form but it doesn't translate well. Reading the Word document will be easier and the links will work.
• Packaging Creative Considerations: The product packaging needs to . . .
• • Have a strong, branded line look.
• - The logo has already been developed, and I would like you to be guided in your design choices by its structure and color, but I am open to deviations from the existing work if it leads to a strong design
• • Use color or some other design elements to distinguish each SKU from the other
• • Be bold and simple. This product will typically be merchandised online, with very small images of the packaging. Simple and bold design elements will ensure that the products are both noticed and understood.
• - The product will likely be contained within white plastic or aluminum (silver) bottles with white caps/pumps. However, if you believe your design concepts would benefit from a particular color of bottle/container, please illustrate that, as that would be possible to execute.
• • Communicate that these products are for pets without using any clichés. This category is full of packaging with stock photos of dogs and cats. Please avoid this at all costs. Instead, please unleash your creativity to illustrate the products’ nature/purposes.
• A couple of packaging designs I would like you to draw inspiration from:
• o Vemo. This line is for human supplements/vitamins. Notice the strong line look, the simple and bold graphics, and the smart use of color and other design elements to differentiate the SKUs (while still holding it together as a single brand.)
• o Tundo. This line is for pets. Again, notice the strong line look, the smart use of color to differentiate the SKUs, and the simple and bold presentation that translates so well on the screen.
• o Corvalune. This design is not as good as the first two, but it does accomplish several of the brief’s objectives and the packaging is likely to be very similar to what your design will eventually be affixed to.
• Design Deliverables: A great submission will illustrate its strength by showing how the design translates across all the expected SKUs. To accomplish, this, I would recommend using the “functional maps” I’ve included in the attached Powerpoint document to:
• o First illustrate, in greater size and detail, one SKU each of the two families (one oil SKU and one supplement SKU)
• o Then illustrate how each of those designs extends across the rest of the family. That illustration can be less detailed. We just need to see how the colors and other design elements extend.
Should not have
• No stock images of cats or dogs; please avoid junking up the designs with too many elements

```html
<!DOCTYPE html>
<html lang="en">
<head>
<meta charset="utf-8">
<title>Kindra – Oil Supplement Labels</title>
<link rel="stylesheet" href="https://fonts.googleapis.com/css2?family=Bebas+Neue&family=Lato:wght@300;400;700;900&family=Oswald:wght@300;400&display=swap">
<style>
  :root {
    --stage: #d6d6d6;
    --ink: #050505;
    --paper: #ffffff;
    --text-dark: #1a1a1a;
    --silver-1: #c2c3c5;
    --silver-2: #f3f3f4;
    --silver-3: #d9dadc;
    --teal: #17adbb;
    --orange: #f7941d;
    --logo-grey: #8a8b8d;
  }
  * { box-sizing: border-box; margin: 0; padding: 0; }
  html, body { width: 1200px; height: 900px; overflow: hidden; }
  body { background: var(--stage); font-family: "Lato", sans-serif; position: relative; }

  .label {
    position: absolute; top: 85px; width: 396px; height: 712px;
    background: var(--ink); border: 1px solid #e8e8e8; overflow: hidden;
  }
  .label--salmon { left: 178px; --accent: var(--teal); }
  .label--omega { left: 616px; --accent: var(--orange); }

  .label__top {
    position: absolute; left: 0; top: 0; width: 100%; height: 291px;
    background: linear-gradient(90deg, var(--silver-1) 0%, var(--silver-2) 30%, var(--silver-2) 55%, var(--silver-3) 80%, var(--silver-1) 100%);
  }
  .label__notch { position: absolute; left: 0; top: 290px; width: 396px; height: 40px; }
  .label__drop { position: absolute; left: 185px; top: 335px; width: 26px; height: 44px; }

  .brand { position: absolute; left: 0; width: 100%; text-align: center; }
  .brand__mark {
    top: 34px; left: 50%; width: 46px; height: 46px; margin-left: -23px;
    border: 3px solid var(--accent-logo, var(--teal)); border-radius: 50%; position: absolute;
  }
  .brand__name {
    top: 88px; font-family: "Lato", sans-serif; font-weight: 300; font-size: 30px;
    color: var(--logo-grey); letter-spacing: 0.5px;
  }

  .kicker {
    position: absolute; left: 0; width: 100%; display: flex; align-items: center; justify-content: center;
    font-family: "Lato", sans-serif; font-weight: 900; color: var(--ink);
  }
  .kicker__rule { height: 2px; background: var(--ink); }
  .kicker--pure { top: 143px; font-size: 32px; letter-spacing: 16px; }
  .kicker--pure .kicker__text { margin-right: -16px; padding: 0 14px 0 14px; }
  .kicker--pure .kicker__rule { width: 70px; }
  .kicker--fish { top: 127px; font-size: 32px; letter-spacing: 3px; }
  .kicker--fish .kicker__text { padding: 0 4px; }
  .kicker--fish .kicker__rule { width: 74px; }

  .product-name {
    position: absolute; left: 0; width: 100%; text-align: center;
    font-family: "Bebas Neue", sans-serif; color: var(--accent); line-height: 1;
  }
  .product-name--salmon { top: 180px; font-size: 89px; letter-spacing: -1px; }
  .product-name--omega { top: 159px; font-size: 112px; letter-spacing: 0; }

  .claim {
    position: absolute; top: 256px; left: 0; width: 100%; text-align: center;
    font-size: 19px; font-weight: 400; color: var(--text-dark);
  }

  .descriptor {
    position: absolute; top: 405px; left: 0; width: 100%; text-align: center;
    color: var(--paper); font-size: 24px; line-height: 30px; font-weight: 400;
  }

  .band { position: absolute; top: 542px; left: 0; width: 100%; height: 28px; background: var(--accent); }
  .seal { position: absolute; top: 511px; left: 153px; width: 90px; height: 90px; }

  .net {
    position: absolute; top: 622px; left: 0; width: 100%; text-align: center;
    font-family: "Oswald", sans-serif; font-weight: 300; font-size: 23px; color: var(--paper);
  }
  .origin {
    position: absolute; top: 661px; left: 0; width: 100%; text-align: center;
    font-size: 13px; letter-spacing: 3px; color: var(--accent); font-weight: 400;
  }
</style>
</head>
<body>

<section class="label label--salmon" aria-label="Pure Salmon Oil label">
  <div class="label__top"></div>
  <svg class="label__notch" viewBox="0 0 396 40" aria-hidden="true">
    <defs>
      <linearGradient id="silver-notch" x1="0" x2="1"><stop offset="0" stop-color="#e2e3e4"/><stop offset="1" stop-color="#eeeeef"/></linearGradient>
    </defs>
    <path d="M150 0 C186 0 190 16 198 36 C206 16 210 0 246 0 Z" fill="url(#silver-notch)"/>
  </svg>
  <svg class="label__drop" viewBox="0 0 26 44" aria-hidden="true">
    <defs>
      <linearGradient id="drop-shine" x1="0" x2="1"><stop offset="0" stop-color="#ffffff"/><stop offset="1" stop-color="#b9babc"/></linearGradient>
    </defs>
    <path d="M13 0 C16 12 26 22 26 31 A13 13 0 0 1 0 31 C0 22 10 12 13 0 Z" fill="url(#drop-shine)"/>
  </svg>

  <div class="brand brand__mark"></div>
  <div class="brand brand__name">Kindra</div>

  <div class="kicker kicker--pure"><span class="kicker__rule"></span><span class="kicker__text">PURE</span><span class="kicker__rule"></span></div>
  <h1 class="product-name product-name--salmon">SALMON OIL</h1>
  <p class="claim">SUPPORTS HEALTHY COAT &amp; SKIN</p>

  <p class="descriptor">ALL NATURAL SUPPLEMENT<br>for DOG &amp; CAT</p>

  <div class="band"></div>
  <svg class="seal" viewBox="0 0 90 90" role="img" aria-label="Made with 100% wild Alaskan salmon seal">
    <defs><path id="ring-salmon" d="M45 45 m-34 0 a34 34 0 1 1 68 0 a34 34 0 1 1 -68 0"/></defs>
    <circle cx="45" cy="45" r="44" fill="#050505"/>
    <circle cx="45" cy="45" r="41" fill="none" stroke="#17adbb" stroke-width="1.5"/>
    <circle cx="45" cy="45" r="25" fill="#ffffff"/>
    <text font-family="Lato, sans-serif" font-size="8.5" fill="#ffffff" letter-spacing="1">
      <textPath href="#ring-salmon" startOffset="2%">WILD ALASKAN SALMON • MADE WITH •</textPath>
    </text>
    <text x="45" y="46" text-anchor="middle" font-family="Oswald, sans-serif" font-size="16" fill="#050505">100%</text>
  </svg>

  <p class="net">Net 32 FL OZ / 946 ML</p>
  <p class="origin">MADE IN USA</p>
</section>

<section class="label label--omega" aria-label="Fish Oil Omega 3 label">
  <div class="label__top"></div>
  <svg class="label__notch" viewBox="0 0 396 40" aria-hidden="true">
    <path d="M150 0 C186 0 190 16 198 36 C206 16 210 0 246 0 Z" fill="url(#silver-notch)"/>
  </svg>
  <svg class="label__drop" viewBox="0 0 26 44" aria-hidden="true">
    <path d="M13 0 C16 12 26 22 26 31 A13 13 0 0 1 0 31 C0 22 10 12 13 0 Z" fill="url(#drop-shine)"/>
  </svg>

  <div class="brand brand__mark"></div>
  <div class="brand brand__name">Kindra</div>

  <div class="kicker kicker--fish"><span class="kicker__rule"></span><span class="kicker__text">FISH OIL</span><span class="kicker__rule"></span></div>
  <h1 class="product-name product-name--omega">OMEGA 3</h1>
  <p class="claim">SUPPORTS HEALTHY COAT &amp; SKIN</p>

  <p class="descriptor">ALL NATURAL SUPPLEMENT<br>for DOG &amp; CAT</p>

  <div class="band"></div>
  <svg class="seal" viewBox="0 0 90 90" role="img" aria-label="Made with 100% Atlantic sardines and anchovies seal">
    <defs><path id="ring-omega" d="M45 45 m-34 0 a34 34 0 1 1 68 0 a34 34 0 1 1 -68 0"/></defs>
    <circle cx="45" cy="45" r="44" fill="#050505"/>
    <circle cx="45" cy="45" r="41" fill="none" stroke="#f7941d" stroke-width="1.5"/>
    <circle cx="45" cy="45" r="25" fill="#ffffff"/>
    <text font-family="Lato, sans-serif" font-size="7" fill="#ffffff" letter-spacing="0.5">
      <textPath href="#ring-omega" startOffset="1%">ATLANTIC SARDINES &amp; ANCHOVIES • MADE WITH •</textPath>
    </text>
    <text x="45" y="46" text-anchor="middle" font-family="Oswald, sans-serif" font-size="16" fill="#050505">100%</text>
  </svg>

  <p class="net">Net 32 FL OZ / 946 ML</p>
  <p class="origin">MADE IN USA</p>
</section>

</body>
</html>
```